Roaming outings business card

please see website
www.roamingoutings.comau

info needed on card
Keiran Voss
Ph
email
Adventure Riding GPS trails

please use my logo and colours off my site

Business

Keiran Voss
keiran@roamingoutings.com

```html
<!DOCTYPE html>
<html lang="en">
<head>
<meta charset="utf-8">
<title>Roaming Outings – Business Card</title>
<link rel="stylesheet" href="https://fonts.googleapis.com/css2?family=Source+Sans+3:ital,wght@0,400;0,600;0,700;1,600&display=swap">
<style>
  :root {
    --page-bg: #4d4d4d;
    --card-bg: #f6f6f6;
    --ink: #1a1a1a;
    --panel: #000000;
    --accent: #f7e21b;
    --text-light: #ffffff;
  }
  html, body {
    margin: 0;
    padding: 0;
    width: 1200px;
    height: 750px;
    overflow: hidden;
    background: var(--page-bg);
    font-family: "Source Sans 3", sans-serif;
  }
  .canvas {
    position: relative;
    width: 1200px;
    height: 750px;
  }
  .card {
    position: absolute;
    left: 150px;
    top: 118px;
    width: 900px;
    height: 514px;
    background: var(--card-bg);
    overflow: hidden;
  }
  .contact-panel {
    position: absolute;
    left: -25px;
    top: 181px;
    width: 450px;
    height: 450px;
    border-radius: 50%;
    background: var(--panel);
  }
  .brand {
    position: absolute;
    left: 560px;
    top: 62px;
    display: flex;
    align-items: center;
    gap: 22px;
  }
  .brand-dot {
    width: 64px;
    height: 64px;
    border-radius: 50%;
    background: var(--accent);
  }
  .brand-name {
    margin: 0;
    font-weight: 700;
    font-size: 44px;
    line-height: 1;
    color: var(--ink);
    text-transform: uppercase;
    letter-spacing: 0.5px;
  }
  .brand-name span { display: block; }
  .contact {
    position: absolute;
    left: 39px;
    top: 278px;
    color: var(--text-light);
  }
  .contact-name {
    margin: 0 0 18px;
    font-weight: 600;
    font-size: 32px;
    line-height: 1.2;
    color: var(--accent);
  }
  .contact-list {
    list-style: none;
    margin: 0;
    padding: 0;
  }
  .contact-item {
    display: flex;
    align-items: center;
    gap: 12px;
    height: 36px;
    font-size: 21px;
  }
  .contact-icon {
    width: 24px;
    height: 24px;
    flex: none;
  }
  .tagline {
    margin: 14px 0 0;
    font-style: italic;
    font-weight: 600;
    font-size: 25px;
    color: var(--accent);
    letter-spacing: 0.5px;
  }
</style>
</head>
<body>
<main class="canvas">
  <section class="card">
    <div class="contact-panel"></div>

    <header class="brand">
      <div class="brand-dot"></div>
      <h1 class="brand-name"><span>Roaming</span><span>Outings</span></h1>
    </header>

    <div class="contact">
      <h2 class="contact-name">Keiran Voss</h2>
      <ul class="contact-list">
        <li class="contact-item">
          <svg class="contact-icon" viewBox="0 0 24 24" aria-hidden="true">
            <path fill="var(--accent)" d="M6.6 10.8c1.4 2.8 3.8 5.1 6.6 6.6l2.2-2.2c.3-.3.7-.4 1-.2 1.1.4 2.3.6 3.6.6.6 0 1 .4 1 1V20c0 .6-.4 1-1 1C10.6 21 3 13.4 3 4c0-.6.4-1 1-1h3.5c.6 0 1 .4 1 1 0 1.3.2 2.5.6 3.6.1.3 0 .7-.2 1z"/>
          </svg>
          <span>613 552 8190</span>
        </li>
        <li class="contact-item">
          <svg class="contact-icon" viewBox="0 0 24 24" aria-hidden="true">
            <rect x="2" y="5" width="20" height="14" rx="1" fill="var(--accent)"/>
            <path d="M2.5 5.5 12 13l9.5-7.5" fill="none" stroke="var(--panel)" stroke-width="1.6"/>
          </svg>
          <span>keiran@roamingoutings.com</span>
        </li>
        <li class="contact-item">
          <svg class="contact-icon" viewBox="0 0 24 24" aria-hidden="true">
            <circle cx="12" cy="12" r="10" fill="var(--accent)"/>
            <path d="M12 2v20M2 12h20M12 2c-4 3-4 17 0 20M12 2c4 3 4 17 0 20" fill="none" stroke="var(--panel)" stroke-width="1.3"/>
          </svg>
          <span>www.roamingoutings.comau</span>
        </li>
      </ul>
      <p class="tagline">Adventure Riding GPS trails</p>
    </div>
  </section>
</main>
</body>
</html>
```